Illustration Design Project

We need two simple, clean circle illustrations of the Hero's Journey that use our terminology. These will be used for Power Point presentations and other paper support docs as part of our programs that help writers, authors, and thought leaders create and shape their books.

We would like to see designs that
- have a white or off-white background complemented with our branded orange and red
- divided according to the attached illustration into 3 Acts
- move clock wise (not counter-clock wise)

The final design should communicate adventure and courage.

Designers should visit bristle harbor.com to understand the company branding colors and logos.

Target Market(s)

writers, authors, thought leaders, coaches, business people who are writing books

Industry/Entity Type

It Company

Requirements
Must have
• - have a white or off-white background complemented with our branded orange and red
- be super-clean and easy-to-read
Nice to have
• nothing too fancy - but if you have an idea to evoke courage without it being corny, that would be fine
Should not have
• Do not go for cliched "journey"-like images.

```html
<!DOCTYPE html>
<html lang="en">
<head>
<meta charset="utf-8">
<title>The Hero's Journey – Three Act Circle</title>
<link href="https://fonts.googleapis.com/css2?family=Open+Sans:ital,wght@0,400;0,700;1,700&display=swap" rel="stylesheet">
<style>
  :root {
    --bg: #ffffff;
    --ink: #222222;
    --act1-light: #ef5a3c;
    --act1-dark: #c8281e;
    --act2: #f7a21f;
    --act3: #8c1a1a;
    --act3-light: #b3261e;
    --ordinary: #c8281e;
    --new: #f39a1e;
    --node-num-dark: #3a2a00;
    --divider: #bcbcbc;
  }
  html, body {
    margin: 0;
    padding: 0;
    width: 1200px;
    height: 900px;
    overflow: hidden;
    background: var(--bg);
  }
  .journey-canvas {
    display: block;
    width: 1200px;
    height: 900px;
    font-family: "Open Sans", Arial, sans-serif;
  }
  .stage-label { fill: var(--ink); font-size: 23px; }
  .stage-label.right { text-anchor: end; }
  .stage-label.middle { text-anchor: middle; }
  .world-label { font-size: 27px; font-weight: 700; text-anchor: middle; }
  .world-label.ordinary { fill: var(--ordinary); }
  .world-label.new { fill: var(--new); }
  .act-label { font-size: 26px; font-weight: 700; font-style: italic; text-anchor: middle; }
  .act-label.act1 { fill: var(--act1-dark); }
  .act-label.act2 { fill: var(--act2); }
  .act-label.act3 { fill: var(--act3); }
  .node-number { font-size: 19px; font-weight: 700; text-anchor: middle; dominant-baseline: central; }
  .node-number.light { fill: #ffffff; }
  .node-number.dark { fill: var(--node-num-dark); }
</style>
</head>
<body>
<svg class="journey-canvas" viewBox="0 0 1200 900" xmlns="http://www.w3.org/2000/svg">
  <defs>
    <linearGradient id="act1-gradient" x1="0" y1="0" x2="1" y2="1">
      <stop offset="0" stop-color="var(--act1-light)"/>
      <stop offset="1" stop-color="var(--act1-dark)"/>
    </linearGradient>
    <linearGradient id="act3-gradient" x1="0" y1="1" x2="1" y2="0">
      <stop offset="0" stop-color="var(--act3-light)"/>
      <stop offset="1" stop-color="var(--act3)"/>
    </linearGradient>
    <radialGradient id="node-red" cx="0.4" cy="0.3" r="0.75">
      <stop offset="0" stop-color="#ffe6e0"/>
      <stop offset="0.45" stop-color="#e0604a"/>
      <stop offset="1" stop-color="#9a1c16"/>
    </radialGradient>
    <radialGradient id="node-yellow" cx="0.4" cy="0.3" r="0.75">
      <stop offset="0" stop-color="#fffbe0"/>
      <stop offset="0.5" stop-color="#ffd84a"/>
      <stop offset="1" stop-color="#e59a00"/>
    </radialGradient>
    <linearGradient id="divider-shade" x1="0" y1="0" x2="1" y2="0">
      <stop offset="0" stop-color="var(--divider)" stop-opacity="0"/>
      <stop offset="0.1" stop-color="var(--divider)" stop-opacity="0.8"/>
      <stop offset="0.55" stop-color="var(--divider)" stop-opacity="0.8"/>
      <stop offset="0.8" stop-color="var(--divider)" stop-opacity="0"/>
    </linearGradient>
  </defs>

  <g class="world-divider">
    <rect x="60" y="478" width="1040" height="5" fill="url(#divider-shade)"/>
    <rect x="405" y="484" width="360" height="3" fill="#555555"/>
  </g>

  <g class="act act1-arc">
    <path d="M581,135.2 A315 315 0 0 1 903.1,400.7" fill="none" stroke="url(#act1-gradient)" stroke-width="33"/>
    <polygon points="936.7,395.4 869.5,406 906.9,444.5" fill="var(--act1-dark)"/>
  </g>
  <g class="act act2-arc">
    <path d="M906.6,466.5 A315 315 0 0 1 296,557.7" fill="none" stroke="var(--act2)" stroke-width="33"/>
    <polygon points="264,569.4 327.9,546.1 282.8,510.1" fill="var(--act2)"/>
  </g>
  <g class="act act3-arc">
    <path d="M277.2,461 A315 315 0 0 1 537.3,139.8" fill="none" stroke="url(#act3-gradient)" stroke-width="33"/>
    <polygon points="531.4,106.3 543.2,173.3 586.5,135.1" fill="var(--act3)"/>
  </g>

  <text class="world-label ordinary" x="592" y="467">The Ordinary World</text>
  <text class="world-label new" x="592" y="519">The New World</text>

  <text class="act-label act1" transform="translate(738 222) rotate(40)">ACT 1</text>
  <text class="act-label act2" transform="translate(612 700) rotate(-6)">ACT 2</text>
  <text class="act-label act3" transform="translate(408 282) rotate(-55)">ACT 3</text>

  <g class="stage-nodes">
    <g class="node red"><circle cx="592" cy="135" r="20" fill="url(#node-red)" stroke="#ffffff" stroke-width="2"/><text class="node-number light" x="592" y="135">1</text></g>
    <g class="node red"><circle cx="735" cy="169.3" r="20" fill="url(#node-red)" stroke="#ffffff" stroke-width="2"/><text class="node-number light" x="735" y="169.3">2</text></g>
    <g class="node red"><circle cx="833.3" cy="247.5" r="20" fill="url(#node-red)" stroke="#ffffff" stroke-width="2"/><text class="node-number light" x="833.3" y="247.5">3</text></g>
    <g class="node red"><circle cx="893.2" cy="357.9" r="20" fill="url(#node-red)" stroke="#ffffff" stroke-width="2"/><text class="node-number light" x="893.2" y="357.9">4</text></g>
    <g class="node yellow"><circle cx="902.2" cy="504.7" r="20" fill="url(#node-yellow)" stroke="#6a4a00" stroke-width="2"/><text class="node-number dark" x="902.2" y="504.7">5</text></g>
    <g class="node yellow"><circle cx="859.1" cy="616.9" r="20" fill="url(#node-yellow)" stroke="#6a4a00" stroke-width="2"/><text class="node-number dark" x="859.1" y="616.9">6</text></g>
    <g class="node yellow"><circle cx="772.7" cy="708" r="20" fill="url(#node-yellow)" stroke="#6a4a00" stroke-width="2"/><text class="node-number dark" x="772.7" y="708">7</text></g>
    <g class="node yellow"><circle cx="592" cy="765" r="20" fill="url(#node-yellow)" stroke="#6a4a00" stroke-width="2"/><text class="node-number dark" x="592" y="765">8</text></g>
    <g class="node yellow"><circle cx="357.9" cy="660.8" r="20" fill="url(#node-yellow)" stroke="#6a4a00" stroke-width="2"/><text class="node-number dark" x="357.9" y="660.8">9</text></g>
    <g class="node red"><circle cx="277" cy="450" r="20" fill="url(#node-red)" stroke="#ffffff" stroke-width="2"/><text class="node-number light" x="277" y="450">10</text></g>
    <g class="node red"><circle cx="313.9" cy="302.1" r="20" fill="url(#node-red)" stroke="#ffffff" stroke-width="2"/><text class="node-number light" x="313.9" y="302.1">11</text></g>
    <g class="node red"><circle cx="425.1" cy="182.9" r="20" fill="url(#node-red)" stroke="#ffffff" stroke-width="2"/><text class="node-number light" x="425.1" y="182.9">12</text></g>
  </g>

  <g class="stage-labels">
    <text class="stage-label" x="577" y="100">The Ordinary World</text>
    <text class="stage-label" x="785" y="162">The Call to Adventure</text>
    <text class="stage-label" x="875" y="255">Refusal of the Call</text>
    <text class="stage-label" x="940" y="363">Meeting</text>
    <text class="stage-label" x="940" y="397">with Mentor</text>
    <text class="stage-label" x="940" y="501">Crossing the First</text>
    <text class="stage-label" x="940" y="535">Threshold</text>
    <text class="stage-label" x="920" y="621">Test, Allies,</text>
    <text class="stage-label" x="920" y="655">Enemies</text>
    <text class="stage-label" x="762" y="752">Approach to</text>
    <text class="stage-label" x="762" y="786">the Inmost Cave</text>
    <text class="stage-label middle" x="590" y="819">Supreme Ordeal</text>
    <text class="stage-label right" x="312" y="684">Reward</text>
    <text class="stage-label right" x="382" y="720">(Seizing the Sword)</text>
    <text class="stage-label right" x="250" y="418">The Road</text>
    <text class="stage-label right" x="250" y="452">Back</text>
    <text class="stage-label right" x="280" y="313">Resurrection</text>
    <text class="stage-label right" x="362" y="176">Return with</text>
    <text class="stage-label right" x="362" y="210">the Elixir</text>
  </g>
</svg>
</body>
</html>
```